Creative, Modern and Conversion based Web Design

Kolvex Digital has recently launched a new logo and as part of our companies rebranding, we need a new website aimed towards the UK B2B marketplace.

The website needs to deliver a modern and creative website design whilst ensuring the design is tailored towards conversion optimisation.

This site must drive point of contact either from an online form, via a direct telephone call or Skype connection.

Our sales are all offline so the website will be a simple, elegant and stunning information portal.

Kolvex Digital offers Digital Marketing services to companies throughout the UK - our target audiences are companies that turnover a minimum of 3 million pounds a year and as such we need to deliver a professional image that installs confidence in our companies abilities.

We do not like websites that are reliant upon stock photography - we are happy for stock photography to be used in a small way however the site must not look like a template filled with stock photography.

What do we do

We supply digital marketing services to those companies who demand a strong return on investment - our company prides itself on delivering successful campaigns that help establish long-term profitable relationships.

A lot of the information presented on our old site is relevant today however the design sucks. So please use the information on our current website as a foundation for your design content.

I am looking for several page designs including

"Home Page" Desktop Version
"Service Page" Desktop Version
"Blog Page" Desktop Version

"Home Page" Mobile Version
"Service Page" Mobile Version
"Blog Page" Mobile Version

In the 1st instance please only submit a single design for the "Home Page" Desktop Version - those designers that we are impressed with will be asked to complete the other designs before a winner is selected.

I like modern clean fonts - the site needs to welcome the reader and encourage them to absorb the information - not to overload and make them leave.

The site must be designed to naturally fit our companies new logo.

NO TEMPLATES

Target Market(s)

B2b - 3 million turnover and above

Industry/Entity Type

Digital Marketing

Number of Pages Required

3 page

Requirements
Must have
• Blended well with the companies logo
• We need conversion optimisation to be a huge part of the design - we considered a conversation when a potential customer reaches out to use via - web form, telephone or skype
• The current content on the old website fits today's business but the design sucks.
• www.kolvexdigital-example.com
Nice to have
• We need 3 pages (in 2 variants Desktop and Mobile)
• Home Page
• Service Page
• Blog Page
• Please only deliver the "Home Page" desktop version - if we are happy with your design we will aks for the additional pages
Should not have
• No templates and not stock photo heavy design

```html
<!DOCTYPE html>
<html lang="en">
<head>
<meta charset="utf-8">
<title>Kolvex Digital – Search Marketing That Actually Delivers</title>
<link href="https://fonts.googleapis.com/css2?family=Open+Sans:wght@300;400;600;700;800&display=swap" rel="stylesheet">
<style>
:root{
  --blue:#0d4fa0;
  --blue-hero:#1c5f9c;
  --blue-deep:#16466f;
  --blue-stats:#1d5cc4;
  --ink:#333;
  --grey-text:#6d6d6d;
  --grey-head:#5a5a5a;
  --grey-bg:#ececec;
  --grey-line:#9a9a9a;
  --grey-cta:#a6a6a6;
  --dark-card:#333333;
  --white:#fff;
}
*{margin:0;padding:0;box-sizing:border-box}
html,body{width:1200px;height:2535px;overflow:hidden;background:var(--white)}
body{position:relative;font-family:"Open Sans",Arial,sans-serif;color:var(--ink)}
.abs{position:absolute}

/* header */
.brand{left:81px;top:14px;display:flex;align-items:center;gap:12px}
.brand-mark{width:34px;height:34px;background:var(--grey-head)}
.brand-name{font-size:30px;font-weight:700;color:var(--grey-head);letter-spacing:.5px}
.top-contacts{right:80px;top:9px;display:flex;gap:34px;font-size:11px;color:#222;align-items:center}
.top-contacts span{display:flex;align-items:center;gap:8px}
.main-nav{right:80px;top:74px;display:flex;gap:30px;font-size:12px;font-weight:700;color:#111}

/* hero */
.hero{left:0;top:97px;width:1200px;height:385px;background:var(--blue-hero)}
.hero-band{left:0;top:436px;width:1200px;height:46px;background:var(--blue-deep)}
.hero-art{left:20px;top:104px;width:540px;height:370px;border-radius:50% 50% 0 0;background:radial-gradient(circle at 50% 55%,#f08a25 0,#2f7fc2 38%,#1c5f9c 70%)}
.hero-title{left:563px;top:162px;color:var(--white);line-height:1}
.hero-title .l1{font-size:55px;font-weight:800;letter-spacing:.5px}
.hero-title .l2{font-size:44px;font-weight:300;letter-spacing:2.5px;margin-top:6px}
.hero-rule{left:563px;top:280px;width:558px;height:2px;background:var(--white)}
.hero-sub{left:582px;top:292px;width:540px;font-size:23px;color:var(--white);line-height:1.3}
.btn-white{left:963px;top:372px;width:154px;height:35px;background:var(--white);color:var(--blue);font-weight:700;font-size:16px;display:flex;align-items:center;justify-content:center;letter-spacing:.5px}

/* intro */
.roi-head{left:81px;top:526px;font-size:25px;font-weight:700;color:var(--grey-head);line-height:1.2}
.roi-head .roi{color:var(--blue);font-size:37px;font-weight:800}
.roi-head .spaced{letter-spacing:5px;font-weight:400}
.partner-badge{left:81px;top:722px;width:253px;height:90px;border:1px solid #ccc;background:#fafafa}
.partner-badge::before{content:"";position:absolute;left:0;top:0;width:8px;height:100%;background:#4a7fd0}
.mini-badges{left:95px;top:816px;display:flex;gap:40px}
.mini-badges div{width:100px;height:34px;background:#e4e4e4;border-radius:4px}
.intro-copy{left:389px;top:527px;width:290px;font-size:12.2px;line-height:21.5px;color:#444;text-align:justify}
.know-rule{left:389px;top:828px;width:28px;height:3px;background:var(--blue)}
.know-link{left:389px;top:843px;font-size:10px;font-weight:700;letter-spacing:3px;color:var(--blue)}
.partner-card{left:705px;top:482px;width:414px;height:385px;border:1px solid #ccc;background:var(--white)}
.partner-card-head{height:102px;background:var(--dark-card);color:var(--white);text-align:center;padding-top:22px}
.partner-card-head h3{font-size:20px;font-weight:700}
.partner-card-head p{font-size:12px;line-height:1.25;margin-top:2px}
.partner-grid{display:grid;grid-template-columns:repeat(3,137px);grid-template-rows:repeat(2,140px)}
.tile{display:flex;align-items:center;justify-content:center}
.tile i{display:block;width:46px;height:46px;border-radius:50%}

/* services */
.services{left:0;top:904px;width:1200px;height:752px;background:var(--grey-bg)}
.services-title{left:0;top:925px;width:1200px;text-align:center;font-size:32px;font-weight:300;color:#333}
.svc-vline{width:2px;background:#999}
.svc-hline{left:98px;top:1313px;width:1004px;height:1px;background:#999}
.svc{width:340px;text-align:center}
.svc svg{display:block;margin:0 auto}
.svc h4{font-size:15.5px;font-weight:700;color:var(--blue);margin-top:14px}
.svc p{font-size:12.4px;line-height:19px;color:#777;margin:10px auto 0;width:270px;height:78px}
.svc .btn{display:inline-block;margin-top:12px;width:176px;height:36px;line-height:36px;background:var(--blue);color:var(--white);font-size:13.5px;font-weight:700}

/* link placements */
.lp-title{left:81px;top:1690px;font-size:30px;font-weight:400;color:#222}
.lp-sub{left:81px;top:1735px;font-size:18px;color:var(--blue)}
.lp-copy{left:81px;top:1788px;width:700px;font-size:11.6px;line-height:21px;color:#666}
.lp-how{left:81px;top:1884px;font-size:11.6px;font-weight:700;color:#666}
.lp-list{left:81px;top:1916px;width:700px;list-style:none;font-size:11.6px;line-height:19px;color:#666}
.lp-list li{position:relative;padding-left:17px;margin-bottom:14px}
.lp-list li::before{content:"";position:absolute;left:0;top:6px;width:7px;height:7px;border-radius:50%;background:var(--blue)}
.btn-blue{left:81px;top:2113px;width:277px;height:37px;background:var(--blue);color:var(--white);font-size:13.5px;font-weight:700;display:flex;align-items:center;justify-content:center}
.stats{left:815px;top:1698px;width:304px;height:454px;background:var(--blue-stats)}
.stats-head{left:853px;top:1730px;color:var(--white);font-size:24px;font-weight:700;line-height:1.12}
.stats-head .sm{font-size:19px}
.stat{left:858px;width:217px;height:68px;border:2px solid rgba(255,255,255,.85);display:flex;align-items:center;padding-left:12px;color:var(--white);gap:6px}
.stat b{font-size:44px;font-weight:700;letter-spacing:-1px}
.stat span{font-size:15px;font-weight:600;line-height:1.05}

/* footer */
.footer-rule{left:0;top:2219px;width:1200px;height:1px;background:#888}
.f-col{top:2219px;height:274px;padding:22px 0 0 0;font-size:12.4px;line-height:23px;color:#333}
.f-div{top:2219px;width:1px;height:274px;background:#888}
.f-col h5{font-size:12px;font-weight:700;color:var(--blue);margin-bottom:8px}
.f-col .lbl{color:var(--blue);font-weight:700}
.f-office{width:200px}
.f-office .email{margin-top:7px;font-size:11.6px;line-height:17px;word-break:break-all}
.social{display:flex;gap:13px;margin-top:10px}
.social i{display:block;width:30px;height:30px;border:1px solid #bbb;background:#f3f3f3}
.cta{left:815px;top:2219px;width:304px;height:274px;background:var(--grey-cta);color:var(--white);text-align:center}
.cta h4{font-size:22px;font-weight:700;line-height:1.05;margin-top:22px}
.cta h4 .big{font-size:29px}
.cta h4 .sm{font-size:18px}
.cta p{font-size:14px;font-weight:600;line-height:20px;text-align:left;padding:0 24px;margin-top:12px}
.cta .btn{display:inline-block;margin-top:24px;width:204px;height:37px;line-height:37px;background:var(--blue);font-size:16px;font-weight:700}
.copyright{left:0;top:2509px;width:1200px;text-align:center;font-size:12px;font-weight:600;color:#999}
</style>
</head>
<body>

<!-- header -->
<div class="abs brand"><span class="brand-mark"></span><span class="brand-name">Kolvex Digital</span></div>
<div class="abs top-contacts">
  <span><svg width="14" height="14" viewBox="0 0 24 24"><path fill="#1a4f8f" d="M6.6 10.8a15 15 0 0 0 6.6 6.6l2.2-2.2c.3-.3.7-.4 1-.2 1.1.4 2.3.6 3.6.6.6 0 1 .4 1 1V20c0 .6-.4 1-1 1A17 17 0 0 1 3 4c0-.6.4-1 1-1h3.5c.6 0 1 .4 1 1 0 1.3.2 2.5.6 3.6.1.3 0 .7-.2 1z"/></svg>+44 (0) 1632 960512</span>
  <span><svg width="18" height="13" viewBox="0 0 18 13"><rect width="18" height="13" fill="#1a4f8f"/><path d="M1 1l8 6 8-6" stroke="#fff" fill="none" stroke-width="1.4"/></svg>info@kolvexdigital-example.com</span>
  <span><svg width="14" height="14"><circle cx="7" cy="7" r="7" fill="#2a9fd8"/></svg>kolvexdigital</span>
</div>
<nav class="abs main-nav"><span>HOME</span><span>SERVICES</span><span>WHITE LABEL LINK BUILDING</span></nav>

<!-- hero -->
<section class="abs hero"></section>
<div class="abs hero-band"></div>
<div class="abs hero-art" role="img" aria-label="Illustration of a rocket launching from a laptop surrounded by marketing icons"></div>
<h1 class="abs hero-title"><div class="l1">SEARCH MARKETING</div><div class="l2">THAT ACTUALLY DELIVERS</div></h1>
<div class="abs hero-rule"></div>
<p class="abs hero-sub">Search Marketing is our forte. Our client results highlight just now good we do it.</p>
<a class="abs btn-white">KNOW MORE</a>

<!-- intro -->
<h2 class="abs roi-head">DO YOU WANT TO SEE<br>AN ENVIABLE <span class="roi">ROI</span><br>ON SEARCH MARKETING?<br><span class="spaced">IT'S POSSIBLE–</span><br>YOU'VE FOUND US</h2>
<div class="abs partner-badge" role="img" aria-label="Search partner certification badge"></div>
<div class="abs mini-badges" role="img" aria-label="Advertising and analytics certification badges"><div></div><div></div></div>
<p class="abs intro-copy">We know and understand the world of business. We know that ROI is the single most important metric in the marketing world. We've worked within some of the world's largest industries – such as finance, insurance, payday loans and health; where achieving above 100% ROI is often impossible. For us, it's just a challenge that can be overcome. Whether we're working with you to drive your Pay-Per-Click Marketing, Organic Search Marketing (SEO), Email Marketing or Lead Filtering &amp; Delivery – we always have your ROI in mind. That's why we're known as the ROI driven digital agency.</p>
<div class="abs know-rule"></div>
<a class="abs know-link">KNOW MORE</a>

<aside class="abs partner-card">
  <div class="partner-card-head">
    <h3>HANDLE YOUR SEO IN-HOUSE?</h3>
    <p>Consider using our industry-leading link outreach service<br>to bolster your efforts.</p>
  </div>
  <div class="partner-grid" role="img" aria-label="Grid of tool and platform certification badges">
    <div class="tile" style="background:#0e8a7a"><i style="background:rgba(255,255,255,.35)"></i></div>
    <div class="tile"><i style="background:#f3a23a"></i></div>
    <div class="tile" style="background:#27a9e1"><i style="background:rgba(255,255,255,.35)"></i></div>
    <div class="tile"><i style="background:#e2622b"></i></div>
    <div class="tile" style="background:#8cbd1f"><i style="background:rgba(255,255,255,.35)"></i></div>
    <div class="tile"><i style="background:#3b78d8"></i></div>
  </div>
</aside>

<!-- services -->
<section class="abs services"></section>
<h2 class="abs services-title">SERVICES WE PROVIDE</h2>
<div class="abs svc-vline" style="left:436px;top:1014px;height:296px"></div>
<div class="abs svc-vline" style="left:774px;top:1014px;height:296px"></div>
<div class="abs svc-vline" style="left:436px;top:1316px;height:310px"></div>
<div class="abs svc-vline" style="left:774px;top:1316px;height:310px"></div>
<div class="abs svc-hline"></div>

<div class="abs svc" style="left:97px;top:1027px">
  <svg width="66" height="66" viewBox="0 0 66 66"><circle cx="30" cy="30" r="24" fill="none" stroke="#555" stroke-width="4"/><rect x="19" y="20" width="22" height="18" fill="none" stroke="#555" stroke-width="3"/><path d="M47 47l14 14" stroke="#555" stroke-width="6"/></svg>
  <h4>ORGANIC SEARCH</h4>
  <p>Attract traffic that converts and interacts with your brand through Organic. We implement both short-term and long-term campaigns to bolster your success.</p>
  <a class="btn">GET TOP RANKING</a>
</div>
<div class="abs svc" style="left:436px;top:1027px">
  <svg width="66" height="66" viewBox="0 0 66 66"><circle cx="30" cy="28" r="24" fill="none" stroke="#555" stroke-width="4"/><circle cx="30" cy="28" r="15" fill="none" stroke="#555" stroke-width="3"/><text x="30" y="34" font-size="17" font-weight="700" text-anchor="middle" fill="#555" font-family="Open Sans,sans-serif">$</text><path d="M40 38l16 24 3-9 9-2z" fill="#555"/></svg>
  <h4>PAID SEARCH</h4>
  <p>Drive highly converting traffic to your website. Our PPC campaigns are ROI-driven from the start – helping you to scale your business quickly.</p>
  <a class="btn">INCREASE LEADS</a>
</div>
<div class="abs svc" style="left:774px;top:1027px">
  <svg width="66" height="66" viewBox="0 0 66 66"><circle cx="33" cy="33" r="28" fill="none" stroke="#555" stroke-width="4"/><rect x="14" y="28" width="20" height="11" rx="5" transform="rotate(-35 24 33)" fill="none" stroke="#555" stroke-width="3"/><rect x="32" y="27" width="20" height="11" rx="5" transform="rotate(-35 42 32)" fill="none" stroke="#555" stroke-width="3"/></svg>
  <h4>LINK OUTREACH</h4>
  <p>The core foundation of any search campaign. Our team of link outreachers are the best in the industry. We secure link placements that drive rankings.</p>
  <a class="btn">SECURE LINK BUILDING</a>
</div>
<div class="abs svc" style="left:97px;top:1342px">
  <svg width="66" height="66" viewBox="0 0 66 66"><path d="M8 6h50L38 30v14H28V30z" fill="none" stroke="#555" stroke-width="3.5"/><circle cx="33" cy="52" r="12" fill="#555"/><text x="33" y="58" font-size="15" font-weight="700" text-anchor="middle" fill="#fff" font-family="Open Sans,sans-serif">$</text></svg>
  <h4>UX &amp; CRO</h4>
  <p>Let us dig into your analytic channels and identify where we can bolster your conversion rates while improving user experience.</p>
  <a class="btn">OPTIMIZE NOW</a>
</div>
<div class="abs svc" style="left:436px;top:1342px">
  <svg width="66" height="66" viewBox="0 0 66 66"><rect x="6" y="30" width="54" height="32" fill="none" stroke="#555" stroke-width="3.5"/><path d="M6 30l27 20 27-20" fill="none" stroke="#555" stroke-width="3.5"/><path d="M30 22l14-10v22z" fill="#555"/><path d="M48 12l6-6M50 20h8M48 28l6 4" stroke="#555" stroke-width="3"/></svg>
  <h4>EMAIL MARKETING</h4>
  <p>Our targeted email marketing campaigns allow you to segment users and deliver custom-tailored campaigns and promotions to different demographics.</p>
  <a class="btn">PROMOTE TO AUDIENCE</a>
</div>
<div class="abs svc" style="left:774px;top:1342px">
  <svg width="66" height="66" viewBox="0 0 66 66"><rect x="6" y="20" width="20" height="16" fill="#555"/><rect x="30" y="4" width="16" height="12" fill="#555"/><rect x="20" y="26" width="40" height="36" fill="#555"/><circle cx="40" cy="38" r="6" fill="#ececec"/><path d="M28 58c2-8 22-8 24 0z" fill="#ececec"/></svg>
  <h4>SOCIAL MEDIA</h4>
  <p>Your followers are your most loyal customers. Let us develop a comprehensive strategy that aligns your brand with interests, while driving increased sales.</p>
  <a class="btn">SOCIAL ADVERTISING</a>
</div>

<!-- link placements -->
<h2 class="abs lp-title">HANDLE SEO YOURSELF? PERFECT.</h2>
<h3 class="abs lp-sub">Hassle-Free Link Placements That Drive Rankings</h3>
<p class="abs lp-copy">Our link placements are used by some of the world's largest companies in the most difficult industries – such as payday loans, insurance, finance, health and legal. We use our link placement service in conjunction with our Organic Search (SEO) offerings; although some of our clients handle their SEO in-house and prefer to use our link placements to bolster their rankings.</p>
<p class="abs lp-how">Here's how our unique, link acquisition process works:</p>
<ul class="abs lp-list">
  <li>We take your clients URLs and their business sector (or your own sites), and we utilise our connections to try and secure a link placement.</li>
  <li>All of the sites we outreach too are 100% genuine – we do not own nor control any of the sites.</li>
  <li>If a webmaster chooses to link to you, it is of their own accord. They have decided to link to you. Thus, you have earned a genuine link.</li>
  <li>We will identify the most relevant page/post on their site, and work with the webmaster to weave your links into their existing content. We will write an additional sentence or two to make sure the anchor text fits in with the content.</li>
</ul>
<a class="abs btn-blue">KNOW MORE AND GET OUR PRICING</a>

<aside class="abs stats"></aside>
<h3 class="abs stats-head">WE GROW AS<br><span class="sm">OUR CLIENTS GROW</span><br><span class="sm">THAT'S WHAT WE LOVE</span></h3>
<div class="abs stat" style="top:1847px"><b>117</b><span>SATISFIED<br>CLIENTS</span></div>
<div class="abs stat" style="top:1944px"><b>215</b><span>CAMPAIGNS<br>FINISHED</span></div>
<div class="abs stat" style="top:2042px"><b>1,798</b><span>CUPS OF<br>COFFEE</span></div>

<!-- footer -->
<div class="abs footer-rule"></div>
<div class="abs f-col" style="left:81px">
  <h5>OUR KEY SERVICES</h5>
  Link Outreach<br>Organic Search (SEO)<br>Paid Search (PPC)<br>Social Media Marketing
  <h5 style="margin-top:34px">FOLLOW US</h5>
  <div class="social" role="img" aria-label="Social network links"><i></i><i></i><i></i></div>
</div>
<div class="abs f-div" style="left:324px"></div>
<div class="abs f-col" style="left:360px">
  <h5>LOCATIONS WE COVER (SEO)</h5>
  Birmingham<br>Essex<br>London<br>Manchester<br>Stoke-on-Trent<br>- See All Locations We Cover (SEO)
</div>
<div class="abs f-div" style="left:569px"></div>
<div class="abs f-col f-office" style="left:604px;line-height:19px">
  <h5>SHREWSBURY OFFICE</h5>
  <span class="lbl">Location :</span> Kolvex Digital Ltd<br>The Granary<br>14 Fenwick Rd<br>Ashby Vale<br>Shrewsbury<br>SY9 4QX<br>
  <div style="margin-top:7px"><span class="lbl">Phone:</span> 01632 960512</div>
  <div class="email"><span class="lbl">Email:</span><br>info@kolvexdigital-example.com</div>
</div>
<aside class="abs cta">
  <h4>WANT TO IMPROVE<br><span class="big">YOUR ROI</span><br><span class="sm">LET'S TALK</span></h4>
  <p>We'll never turn down an opportunity to discover how we can help grow your business.</p>
  <a class="btn">CONTACT US TODAY</a>
</aside>
<p class="abs copyright">© 2018 Kolvex Digital Limited. All rights reserved.</p>

</body>
</html>
```